IT Company based on Biology Business Needs a Business Card Design

We need a business card design for a new company called 'Lumen CELL'. We develop the machine learning solutions especially focused on deep learning algorithms for biology industry. Our initial product is a vision detection on biological images to help doctors diagnose the symptoms. We would like to see designs that use the color green.

Industry/Entity Type

Business

```html
<!DOCTYPE html>
<html lang="en">
<head>
<meta charset="utf-8">
<title>Lumen CELL – Business Card</title>
<link href="https://fonts.googleapis.com/css2?family=Montserrat:wght@400;500;600&display=swap" rel="stylesheet">
<style>
  :root {
    --page-bg: #eef1ee;
    --green-light: #8fd26f;
    --green-mid: #2e9e3c;
    --green-deep: #16782f;
    --green-dark: #0f6a2c;
    --green-accent: #5cbb3f;
    --name-green: #1f9a5a;
    --white: #ffffff;
    --card-shadow: 0 14px 30px rgba(20, 50, 25, 0.22);
  }
  * { margin: 0; padding: 0; box-sizing: border-box; }
  html, body {
    width: 1200px; height: 913px; overflow: hidden;
    background: var(--page-bg);
    font-family: "Montserrat", sans-serif;
  }
  .stage { position: relative; width: 1200px; height: 913px; }
  .card {
    position: absolute; width: 540px; height: 309px;
    border-radius: 4px; overflow: hidden;
    box-shadow: var(--card-shadow);
  }
  /* Front */
  .card-front {
    left: 40px; top: 302px;
    background: linear-gradient(160deg, var(--green-light) 0%, var(--green-mid) 45%, var(--green-deep) 75%, var(--green-dark) 100%);
  }
  .card-front .brand {
    position: absolute; left: 0; right: 0; top: 128px;
    text-align: center; color: var(--white);
    font-size: 38px; font-weight: 500; letter-spacing: 1px;
  }
  .brand-dot {
    display: inline-block; width: 16px; height: 16px; border-radius: 50%;
    margin-right: 14px; vertical-align: 6px;
  }
  .card-front .brand-dot { background: var(--white); }
  /* Back */
  .card-back { left: 620px; top: 302px; background: var(--white); }
  .card-back .waves { position: absolute; inset: 0; width: 100%; height: 100%; }
  .holder { position: absolute; right: 28px; top: 18px; text-align: right; }
  .holder-name {
    color: var(--name-green); font-size: 20px; font-weight: 600; letter-spacing: 0.5px;
  }
  .holder-title { color: var(--green-accent); font-size: 11px; margin-top: 2px; }
  .card-back .brand {
    position: absolute; left: 28px; top: 168px;
    color: var(--green-accent); font-size: 30px; font-weight: 500; letter-spacing: 1px;
  }
  .card-back .brand-dot { width: 14px; height: 14px; margin-right: 12px; vertical-align: 5px; background: var(--green-accent); }
  .contacts {
    position: absolute; right: 22px; top: 145px;
    list-style: none; text-align: right; color: var(--white);
    font-size: 11px; line-height: 21px;
  }
  .contacts li { display: flex; justify-content: flex-end; align-items: center; gap: 7px; }
  .contacts svg { width: 11px; height: 11px; flex: none; }
</style>
</head>
<body>
<main class="stage">
  <section class="card card-front">
    <div class="brand"><span class="brand-dot"></span>Lumen CELL</div>
  </section>

  <section class="card card-back">
    <svg class="waves" viewBox="0 0 540 309" preserveAspectRatio="none" aria-hidden="true">
      <defs>
        <linearGradient id="waveFill" x1="0" y1="0" x2="1" y2="1">
          <stop offset="0" stop-color="#1f9f55"/>
          <stop offset="1" stop-color="#0f7a34"/>
        </linearGradient>
        <path id="waveEdge" d="M540,70 C400,85 330,125 300,195 C270,265 200,305 110,324 L540,324 Z"/>
      </defs>
      <path d="M540,70 C400,85 330,125 300,195 C270,265 200,305 110,324" transform="translate(-30,0)" fill="none" stroke="#a6dd86" stroke-width="2"/>
      <use href="#waveEdge" transform="translate(-18,0)" fill="#7ccf5a"/>
      <use href="#waveEdge" transform="translate(-8,0)" fill="#ffffff"/>
      <use href="#waveEdge" fill="url(#waveFill)"/>
    </svg>

    <div class="holder">
      <div class="holder-name">Your name</div>
      <div class="holder-title">Your Title</div>
    </div>

    <div class="brand"><span class="brand-dot"></span>Lumen CELL</div>

    <ul class="contacts">
      <li>+00 111 222 3333
        <svg viewBox="0 0 12 12"><path d="M3 1 L5 3 L4 5 Q5 7 7 8 L9 7 L11 9 L9.5 11 Q5 11 1 5 Q1 2 3 1 Z" fill="#fff"/></svg>
      </li>
      <li>yourwebsite.com
        <svg viewBox="0 0 12 12"><rect x="1" y="2.5" width="10" height="7" fill="none" stroke="#fff" stroke-width="1.2"/><path d="M1 2.5 L6 7 L11 2.5" fill="none" stroke="#fff" stroke-width="1.2"/></svg>
      </li>
      <li>yourname@yourwebsite.com
        <svg viewBox="0 0 12 12"><circle cx="6" cy="6" r="5" fill="none" stroke="#fff" stroke-width="1.2"/><ellipse cx="6" cy="6" rx="2.2" ry="5" fill="none" stroke="#fff" stroke-width="1"/><path d="M1 6 H11" stroke="#fff" stroke-width="1"/></svg>
      </li>
    </ul>
  </section>
</main>
</body>
</html>
```